TovaLamarpe - Israeli Mental Health Website

We are developing an Israeli website for mental health. The website will be both in English and in Hebrew. We have a logo and would like a website design based on the logo and the logos colors (attached).

Attached is a doc that contains the website requirements.

We would like to have an icon for each of the sidebar categories, an image for each of the pages (including each of the sidebar category pages).

Target Market(s)

Adults 18-80

Industry/Entity Type

Mental Health

Number of Pages Required

5+ page

Font styles to use
Sans Serif

Colors

Designer to choose colors to be used in the design.

```html
<!DOCTYPE html>
<html lang="en">
<head>
<meta charset="utf-8">
<title>TovaLamarpe – Organization for Mental Health</title>
<link href="https://fonts.googleapis.com/css2?family=Montserrat:wght@300;400;700;800&family=Inter:wght@400;500;700&display=swap" rel="stylesheet">
<style>
:root{
  --blue:#2a8ae0;
  --blue-dark:#1f72c4;
  --green:#4caf3e;
  --ink:#1e1e1e;
  --text:#3a3a3a;
  --bar:#222222;
  --white:#ffffff;
  --grey:#d8d8d8;
}
*{margin:0;padding:0;box-sizing:border-box}
html,body{width:1200px;height:4108px;overflow:hidden;background:var(--white);font-family:'Inter',sans-serif;color:var(--text)}
.page{position:relative;width:1200px;height:4108px}
.topbar{position:absolute;left:420px;top:0;width:780px;height:40px;background:var(--bar);clip-path:polygon(30px 0,100% 0,100% 100%,0 100%)}
.lang{position:absolute;right:45px;top:8px;display:flex;align-items:center;gap:10px;color:var(--white);font-size:12px;font-weight:500}
.lang .globe{width:24px;height:24px;border-radius:50%;background:var(--blue)}
.brand{position:absolute;left:40px;top:36px;display:flex;align-items:center;gap:16px}
.brand .dot{width:64px;height:64px;border-radius:50%;background:var(--blue)}
.brand .name{font-family:'Montserrat',sans-serif;font-weight:700;font-size:34px;color:var(--blue-dark)}
.nav{position:absolute;left:433px;top:76px;display:flex;gap:0}
.nav a{position:absolute;white-space:nowrap;font-family:'Inter',sans-serif;font-size:10px;font-weight:500;color:var(--ink);text-decoration:none;letter-spacing:.3px}
.donate{position:absolute;left:1058px;top:63px;width:109px;height:40px;border-radius:20px;background:var(--green);color:var(--white);font:700 11px 'Montserrat',sans-serif;display:flex;align-items:center;justify-content:center;letter-spacing:.5px}
.sidebar{position:absolute;left:28px;top:128px;width:99px;height:3880px;background:var(--blue);border-radius:4px}
.sidebar .active{position:absolute;left:12px;top:15px;width:75px;height:72px;background:var(--blue-dark);border-radius:4px}
.sidebar svg{position:absolute;left:37px;width:26px;height:26px}
.tip{position:absolute;left:158px;top:155px;width:124px;height:50px;background:var(--white);box-shadow:2px 2px 6px rgba(0,0,0,.25);font-size:11px;line-height:13px;color:var(--ink);padding:11px 0 0 18px}
.panel{position:absolute;left:160px;width:1007px;overflow:hidden}
.photo{position:absolute;inset:0}
.edge-l{border-left:3px solid var(--green)}
.edge-r{border-right:3px solid var(--green)}
.hero-title{position:absolute;left:0;right:0;top:96px;text-align:center;font-family:'Montserrat',sans-serif;font-size:44px;line-height:50px;color:var(--ink)}
.hero-title .light{font-weight:400}
.hero-title .bold{font-weight:800}
.copy{position:absolute;width:330px}
.copy h2{font-family:'Montserrat',sans-serif;font-size:40px;line-height:46px;color:var(--ink);margin-bottom:30px}
.copy h2 .light{display:block;font-weight:300}
.copy h2 .bold{display:block;font-weight:800}
.copy p{font-size:12px;line-height:20px;color:var(--text);width:310px}
.btn{display:inline-flex;align-items:center;height:40px;padding:0 31px;border-radius:20px;background:var(--green);color:var(--white);font:700 10px 'Montserrat',sans-serif;letter-spacing:.3px;margin-top:43px}
.copy.right{text-align:right}
.copy.right p{margin-left:auto}
.seal{position:absolute;left:604px;width:116px;height:116px;border-radius:50%;background:var(--white);box-shadow:0 2px 8px rgba(0,0,0,.12)}
.link{position:absolute;left:745px;width:23px;height:33px;background:var(--grey)}
.chat{position:absolute;left:1128px;top:400px;width:72px;height:74px;background:var(--green);border-radius:6px 0 0 6px;display:flex;align-items:center;justify-content:center}
.footer{position:absolute;left:0;top:4042px;width:1200px;height:66px;background:var(--bar);color:var(--white);font-size:14px}
.footer .legal{position:absolute;left:125px;top:24px}
.footer .links{position:absolute;left:910px;top:24px;color:#5fa8ff}
.footer .links a{color:#5fa8ff}
</style>
</head>
<body>
<div class="page">
  <div class="topbar"><div class="lang"><span class="globe"></span>English ▾</div></div>

  <div class="brand"><span class="dot"></span><span class="name">TovaLamarpe</span></div>

  <nav class="nav">
    <a style="left:0">SMART CHATLINE</a>
    <a style="left:139px">THERAPISTS</a>
    <a style="left:244px">ORGANIZATIONS</a>
    <a style="left:369px">VIDEOS</a>
    <a style="left:449px">CONTACT</a>
    <a style="left:540px">ABOUT</a>
  </nav>
  <div class="donate">DONATE</div>

  <aside class="sidebar">
    <div class="active"></div>
    <svg style="top:37px" viewBox="0 0 26 26"><circle cx="13" cy="13" r="10" fill="none" stroke="#fff" stroke-width="2.5"/><circle cx="13" cy="13" r="4" fill="#4caf3e"/></svg>
    <svg style="top:101px" viewBox="0 0 26 26"><circle cx="13" cy="16" r="7" fill="none" stroke="#fff" stroke-width="2.5"/><path d="M13 2v7" stroke="#fff" stroke-width="2.5"/></svg>
    <svg style="top:165px" viewBox="0 0 26 26"><circle cx="13" cy="8" r="5" fill="#fff"/><rect x="5" y="15" width="16" height="9" rx="3" fill="#fff"/></svg>
    <svg style="top:229px" viewBox="0 0 26 26"><circle cx="9" cy="9" r="5" fill="#4caf3e"/><circle cx="17" cy="16" r="6" fill="#fff"/></svg>
    <svg style="top:293px" viewBox="0 0 26 26"><circle cx="13" cy="13" r="10" fill="#fff"/><path d="M13 4v18" stroke="#4caf3e" stroke-width="2"/></svg>
    <svg style="top:357px" viewBox="0 0 26 26"><path d="M5 22c0-9 6-15 15-15" fill="none" stroke="#fff" stroke-width="3"/><circle cx="19" cy="7" r="4" fill="#4caf3e"/></svg>
    <svg style="top:421px" viewBox="0 0 26 26"><circle cx="13" cy="9" r="5" fill="#fff"/><path d="M3 20h20" stroke="#4caf3e" stroke-width="3"/></svg>
    <svg style="top:485px" viewBox="0 0 26 26"><path d="M6 22V12a7 7 0 0 1 14 0v10z" fill="#fff"/><circle cx="14" cy="11" r="3" fill="#4caf3e"/></svg>
    <svg style="top:549px" viewBox="0 0 26 26"><circle cx="13" cy="13" r="5" fill="#fff"/><circle cx="13" cy="13" r="10" fill="none" stroke="#4caf3e" stroke-width="2" stroke-dasharray="4 3"/></svg>
    <svg style="top:613px" viewBox="0 0 26 26"><rect x="3" y="12" width="20" height="3" fill="#fff"/><path d="M6 15v8M20 15v8" stroke="#fff" stroke-width="2.5"/><circle cx="13" cy="6" r="4" fill="#4caf3e"/></svg>
    <svg style="top:677px" viewBox="0 0 26 26"><circle cx="12" cy="7" r="4" fill="#fff"/><rect x="5" y="13" width="14" height="10" rx="4" fill="#fff"/><circle cx="20" cy="19" r="3" fill="#4caf3e"/></svg>
    <svg style="top:741px" viewBox="0 0 26 26"><rect x="6" y="4" width="14" height="19" fill="#fff"/><path d="M10 9h6M10 14h6" stroke="#2a8ae0" stroke-width="2"/></svg>
    <svg style="top:805px" viewBox="0 0 26 26"><circle cx="11" cy="11" r="7" fill="#fff"/><circle cx="18" cy="18" r="4" fill="#4caf3e"/></svg>
  </aside>

  <div class="tip">Emergency<br>Mental Help</div>

  <section class="panel edge-l" style="top:128px;height:619px">
    <div class="photo" role="img" aria-label="Person raising joined hands toward the sunset over coastal mountains" style="background:linear-gradient(180deg,#c9ccd2 0%,#e3c9a8 40%,#d88a3c 62%,#5a2f15 85%,#2a1a10 100%)"></div>
    <h1 class="hero-title"><span class="light">BRINGING HOPE TO</span><br><span class="bold">THOSE STRUGGLING WITH<br>MENTAL ILLNESS</span></h1>
  </section>

  <section class="panel edge-r" style="top:780px;height:620px">
    <div class="photo" role="img" aria-label="Close-up of a seated person with clasped hands" style="background:linear-gradient(90deg,#eeeeef 0%,#e6e6e6 35%,#c9c4be 60%,#b8aca3 80%,#8f8f8f 100%)"></div>
    <div class="copy" style="left:70px;top:165px">
      <h2><span class="light">EMERGENCY</span><span class="bold">MENTAL HELP</span></h2>
      <p>Lorem Ipsum is simply dummy text of the printing and typesetting industry. Lorem Ipsum has been the industry's standard dummy text ever since the 1500s, when an unknown printer took a galley of type and scrambled it to make a type</p>
      <span class="btn">MORE OPTIONS FOR EMERGENCY MENTAL HELP</span>
    </div>
  </section>

  <section class="panel edge-l" style="top:1433px;height:619px">
    <div class="photo" role="img" aria-label="Therapist guiding a smiling patient through a stretching exercise" style="background:linear-gradient(90deg,#d9d6d2 0%,#4d8fd0 20%,#e8c8b4 40%,#ecebe9 60%,#f1f1f1 100%)"></div>
    <div class="copy right" style="left:568px;top:185px">
      <h2><span class="bold">THERAPISTS</span></h2>
      <p>Lorem Ipsum is simply dummy text of the printing and typesetting industry. Lorem Ipsum has been the industry's standard dummy text ever since the 1500s, when an unknown printer took a galley of type and scrambled it to make a type</p>
      <span class="btn">FIND THERAPISTS</span>
    </div>
  </section>

  <section class="panel edge-r" style="top:2087px;height:616px">
    <div class="photo" role="img" aria-label="Hands holding a blue smartphone" style="background:linear-gradient(90deg,#ededed 0%,#dcdcdc 40%,#a9a9aa 60%,#cfc6c1 80%,#e7e7e7 100%)"></div>
    <div class="copy" style="left:70px;top:165px">
      <h2><span class="light">SMART</span><span class="bold">CHATLINE</span></h2>
      <p>Lorem Ipsum is simply dummy text of the printing and typesetting industry. Lorem Ipsum has been the industry's standard dummy text ever since the 1500s, when an unknown printer took a galley of type and scrambled it to make a type</p>
      <span class="btn">05X-XXXXXXX</span>
    </div>
  </section>

  <section class="panel edge-l" style="top:2738px;height:619px">
    <div class="photo" role="img" aria-label="Woman receiving therapeutic tape on her shoulder in a bright room" style="background:linear-gradient(90deg,#eaeaea 0%,#6b4a35 25%,#5a9fc9 38%,#e6e8e6 60%,#c9d9bf 100%)"></div>
    <div class="copy right" style="left:568px;top:185px">
      <h2><span class="bold">VIDEOS</span></h2>
      <p>Lorem Ipsum is simply dummy text of the printing and typesetting industry. Lorem Ipsum has been the industry's standard dummy text ever since the 1500s, when an unknown printer took a galley of type and scrambled it to make a type</p>
      <span class="btn">PLAY VIDEO</span>
    </div>
  </section>

  <section class="panel edge-r" style="top:3392px;height:616px">
    <div class="photo" role="img" aria-label="Three colleagues working together around a laptop in an office" style="background:linear-gradient(90deg,#f4f5f6 0%,#eef0f1 40%,#c7b8a6 60%,#4a6f9c 78%,#3c3c3c 92%,#b9d3a2 100%)"></div>
    <div class="copy" style="left:70px;top:165px">
      <h2><span class="light">FIND</span><span class="bold">ORGANIZATION</span></h2>
      <p>Lorem Ipsum is simply dummy text of the printing and typesetting industry. Lorem Ipsum has been the industry's standard dummy text ever since the 1500s, when an unknown printer took a galley of type and scrambled it to make a type</p>
      <span class="btn">FIND ORGANIZATIONS</span>
    </div>
  </section>

  <span class="link" style="top:1400px"></span>
  <span class="link" style="top:2052px"></span>
  <span class="link" style="top:2705px"></span>
  <span class="seal" style="top:705px"></span>
  <span class="seal" style="top:1358px"></span>
  <span class="seal" style="top:2012px"></span>
  <span class="seal" style="top:2664px"></span>
  <span class="seal" style="top:3317px"></span>

  <div class="chat"><svg width="40" height="40" viewBox="0 0 24 24"><circle cx="12" cy="12" r="10" fill="none" stroke="#fff" stroke-width="1.8"/><path d="M8.5 7.5c.5-.5 1.2-.4 1.5.2l.7 1.4c.2.4.1.8-.2 1.1l-.5.5c.6 1.3 1.6 2.3 2.9 2.9l.5-.5c.3-.3.7-.4 1.1-.2l1.4.7c.6.3.7 1 .2 1.5l-.7.7c-3.5.3-7.6-3.8-7.3-7.3z" fill="#fff"/></svg></div>

  <footer class="footer">
    <span class="legal">TovaLamarpe - Organization for Mental Health ©2023</span>
    <span class="links"><a href="#">Privacy Policy</a> &nbsp;|&nbsp; <a href="#">Terms</a></span>
  </footer>
</div>
</body>
</html>
```